Sign Shop website

We need a web design for a sign company called Quillby Signs that builds signs for shops such as A Frames, Banners, Tennet Boards, Shop front windows etc...

The existing site is avaliable at www.quillbysigns.com.au

We will need to have a fresh makeover. The new site must have the following:

Photo Galleries (broken down into sections)
Store Locations (currently there are 4 stores)
Online quote form
List of services
About Us Page

We just need to front page designed in photoshop (the inner page is not necessary) We have a team that can code the site up.

The website should have the exact logo. Any person who alters the logo, design will be elimated.

No Twitter, RSS, LinkedIn icons

The main colours are yellow, black, blue, red

Target Market(s)

Any business

Industry/Entity Type

It Company

Requirements
Must have
• jQuery slider banner
Should not have
• Alter the logo in any way

```html
<!DOCTYPE html>
<html lang="en">
<head>
<meta charset="utf-8">
<title>Quillby Signs</title>
<link rel="stylesheet" href="https://fonts.googleapis.com/css2?family=Noto+Sans:ital,wght@0,400;0,700;1,700&display=swap">
<style>
:root{
  --page:#eef6fa;
  --yellow:#eeb333;
  --red:#e04a26;
  --ink:#111;
  --muted:#555;
  --purple:#5a1a9a;
  --frame:#d4d4d4;
  --field:#f6f8fd;
  --field-line:#d3dde5;
  --grey-head:#7b7b7b;
  --footer:#2a2a33;
}
*{margin:0;padding:0;box-sizing:border-box}
html,body{width:1200px;height:1149px;overflow:hidden}
body{position:relative;background:var(--page);font-family:"Noto Sans",sans-serif;color:var(--ink)}
.abs{position:absolute}
.header-band{left:0;top:49px;width:1200px;height:81px;background:var(--yellow)}
.brand{left:106px;top:20px;display:flex;align-items:center;gap:10px;font-size:34px;font-weight:700;color:var(--purple)}
.brand-mark{width:22px;height:22px;background:var(--red)}
.nav{left:575px;top:76px;height:36px;display:flex;align-items:center;font-size:14px}
.nav a{color:var(--ink);text-decoration:none;padding:0 24px;border-left:2px solid #f7d58a;line-height:36px}
.nav a:first-child{border-left:none;padding:0 24px 0 0}
.nav a.current{color:var(--purple)}
.slider{left:105px;top:151px;width:1006px;height:396px;background:var(--frame);border-radius:10px}
.slide-image{left:116px;top:160px;width:985px;height:378px;background:linear-gradient(120deg,#0a1a3a 0%,#1d5cc7 40%,#2f6fd9 60%,#0b1e48 100%)}
.caption{left:106px;top:359px;width:525px;height:136px;background:rgba(40,44,54,.82);color:#fff;padding:12px 32px}
.caption h2{font-size:20px;font-weight:700;display:inline-block;border-bottom:1px solid var(--yellow);padding-bottom:0;line-height:26px;padding-right:44px}
.caption p{font-size:13.5px;line-height:21px;margin-top:16px}
.controls{left:804px;top:483px;width:283px;height:39px;background:#e8e8e8;border-radius:5px;border:1px solid #c8c8c8}
.welcome{left:0;top:560px;width:1240px;text-align:center;font-size:27px;font-weight:700;color:var(--red)}
.intro{left:126px;top:614px;width:988px;text-align:center;font-size:14px;line-height:21px}
.intro b{color:var(--red);font-weight:700}
.quote-box{left:123px;top:739px;width:717px;height:326px;background:#fff;border:1px solid #e3e8ec}
.quote-head{left:123px;top:701px;width:717px;height:38px;background:var(--red);color:#fff;font-size:22px;font-weight:700;font-style:italic;padding-left:41px;line-height:38px}
.label{font-size:13px;color:var(--muted)}
.field{height:22px;background:var(--field);border:1px solid var(--field-line)}
.submit{left:731px;top:1075px;width:109px;height:27px;background:linear-gradient(#e8502a,#c53a17);color:#fff;font-size:17px;font-weight:700;font-style:italic;text-align:center;line-height:27px}
.gallery-head{left:878px;top:702px;width:240px;height:33px;background:var(--grey-head);color:#fff;font-size:16px;font-weight:700;font-style:italic;padding-left:33px;line-height:33px}
.thumb{width:74px;height:54px;background:#fff;border:1px solid #cfd8de;border-radius:5px}
.gallery-rule{left:878px;top:885px;width:240px;height:5px;background:var(--grey-head)}
.map{left:861px;top:910px;width:268px;height:195px;background:linear-gradient(135deg,#e9e6dc,#ddd8c8);border:3px solid #d0d6da;border-radius:3px}
.footer{left:0;top:1126px;width:1200px;height:23px;background:var(--footer);color:#ddd;font-size:10px;text-align:center;line-height:23px}
</style>
</head>
<body>
<div class="abs header-band"></div>
<div class="abs brand"><span class="brand-mark"></span>Quillby Signs</div>
<nav class="abs nav">
  <a href="#" aria-label="Home"><svg width="18" height="16" viewBox="0 0 18 16" style="vertical-align:middle"><path d="M9 1 1 8h2.5v7h4v-4h3v4h4V8H17z" fill="#111"/></svg></a>
  <a href="#">About Us</a>
  <a href="#">Our Services</a>
  <a href="#" class="current">OurPortfolio</a>
  <a href="#">Contact Us</a>
</nav>

<div class="abs slider"></div>
<div class="abs slide-image" role="img" aria-label="Close-up of a large format sign printer in blue light"></div>
<div class="abs caption">
  <h2>Sign Solution</h2>
  <p>Quillby Signs will exceed customer expectations by offering a personal-ised approach to clients,embracing and execuing individual needs through a comprehensive range of services.</p>
</div>
<div class="abs controls">
  <svg width="283" height="39" viewBox="0 0 283 39">
    <g fill="#444"><circle cx="25" cy="19" r="7"/><circle cx="48" cy="19" r="7"/><circle cx="71" cy="19" r="7"/><circle cx="94" cy="19" r="7"/><circle cx="117" cy="19" r="7"/><circle cx="140" cy="19" r="7"/></g>
    <circle cx="162" cy="19" r="9" fill="#fff" stroke="#444" stroke-width="3"/>
    <path d="M162 10a9 9 0 0 1 9 9" fill="none" stroke="#2a8ad8" stroke-width="3"/>
    <line x1="192" y1="6" x2="192" y2="33" stroke="#c8c8c8"/>
    <path d="M225 11l-7 8 7 8M251 11l7 8-7 8" fill="none" stroke="#333" stroke-width="3.5" stroke-linecap="round" stroke-linejoin="round"/>
  </svg>
</div>

<h1 class="abs welcome">Welcome</h1>
<p class="abs intro"><b>Quillby Signs</b> is a West Australian owned and managed company. We manufacture signage for any application; vinyl lettering, pull up ban-ners, vehicle signage, in fact anything that requires our customers seeing the full picture when it comes to advertising their business. So if you're serious about the best, put us to the test!</p>

<div class="abs quote-box"></div>
<div class="abs quote-head">Request a Quote</div>
<span class="abs label" style="left:162px;top:759px">Name:</span><div class="abs field" style="left:279px;top:759px;width:185px"></div>
<span class="abs label" style="left:162px;top:796px">Company:</span><div class="abs field" style="left:279px;top:795px;width:185px"></div>
<span class="abs label" style="left:162px;top:832px">Phone:</span><div class="abs field" style="left:279px;top:831px;width:185px"></div>
<span class="abs label" style="left:162px;top:869px">Email Address:</span><div class="abs field" style="left:279px;top:867px;width:185px"></div>
<span class="abs label" style="left:162px;top:905px">Suburb:</span><div class="abs field" style="left:279px;top:904px;width:185px"></div>
<span class="abs label" style="left:162px;top:942px">Store:</span><div class="abs field" style="left:279px;top:940px;width:185px"></div>
<span class="abs label" style="left:504px;top:760px">Sign Type:</span><div class="abs field" style="left:644px;top:759px;width:184px"></div>
<span class="abs label" style="left:504px;top:797px">Material:</span><div class="abs field" style="left:644px;top:797px;width:184px"></div>
<span class="abs label" style="left:504px;top:833px">Sign Size:</span><div class="abs field" style="left:644px;top:833px;width:184px"></div>
<span class="abs label" style="left:504px;top:870px">Artwork Required:</span><div class="abs field" style="left:644px;top:868px;width:184px"></div>
<span class="abs label" style="left:504px;top:906px">Other Information</span><div class="abs field" style="left:506px;top:929px;width:322px;height:123px"></div>
<div class="abs submit">Submit</div>

<div class="abs gallery-head">Photo Gallery</div>
<div class="abs thumb" style="left:879px;top:753px"></div>
<div class="abs thumb" style="left:959px;top:753px"></div>
<div class="abs thumb" style="left:1041px;top:753px"></div>
<div class="abs thumb" style="left:878px;top:820px"></div>
<div class="abs thumb" style="left:958px;top:820px"></div>
<div class="abs thumb" style="left:1040px;top:820px"></div>
<div class="abs gallery-rule"></div>
<div class="abs map" role="img" aria-label="Street map showing the store locations"></div>

<footer class="abs footer">© 2013 Quillby Signs</footer>
</body>
</html>
```